PowerPoint Design Project

We need a powerpoint design for our consulting company, Brindle Consulting. We provide technology strategy and solutioning services, with an emphasis on cloud technology. More information about our services can be found at www.brindleconsulting-example.com

We are looking for a design that is professional, but not corporate stuffy. The design needs to use our primary colors in our brand.
Updates

Reason: We need to iterate on some of the great designs, plus, many people have not had a chance to submit their design yet.

Reason: We had a lot of people accept the project, but not all of them have responded yet. We wanted to get them some time, plus, ask a couple of people to make some minor revisions.

Target Market(s)

Technology buyers between the ages of 30-55 at Vantor 1000 companies

Industry/Entity Type

It Company

Requirements
Must have
• Must follow our logo colors.
Must have at least a cover slide and interior content slide.
Should not have
• Should not contain anything cartoonish or anything with lots of clouds

```html
<!DOCTYPE html>
<html lang="en">
<head>
<meta charset="utf-8">
<title>Project Title – Brindle Consulting</title>
<link href="https://fonts.googleapis.com/css2?family=Arimo:wght@400;700&family=PT+Sans:wght@400&display=swap" rel="stylesheet">
<style>
  :root {
    --bg-light: #f4f4f4;
    --bg-mid: #eeeeee;
    --bg-dark: #e4e4e4;
    --brown: #7a6b5e;
    --brown-text: #6b5e54;
    --teal: #3d7b7f;
    --brand-blue: #2a9fd0;
    --table-head: #cfcac5;
    --footer-text: #c9beb4;
    --page-box: #cdc9c4;
  }
  * { margin: 0; padding: 0; box-sizing: border-box; }
  html, body { width: 1200px; height: 900px; overflow: hidden; }
  body { font-family: "Arimo", Arial, sans-serif; }

  .slide {
    position: relative;
    width: 1200px;
    height: 900px;
    overflow: hidden;
    background: var(--bg-light);
  }

  .backdrop {
    position: absolute;
    inset: 0;
    background: linear-gradient(160deg, var(--bg-light) 0%, var(--bg-mid) 55%, var(--bg-dark) 100%);
  }

  .slide-title {
    position: absolute;
    left: 64px;
    top: 43px;
    font-size: 33px;
    font-weight: 700;
    color: var(--brown);
    letter-spacing: 0.3px;
  }
  .header-rule {
    position: absolute;
    left: 0;
    top: 90px;
    width: 1200px;
    height: 2px;
    background: var(--brown);
  }

  .brand {
    position: absolute;
    right: 28px;
    top: 38px;
    display: flex;
    align-items: center;
    gap: 12px;
  }
  .brand-mark {
    width: 22px;
    height: 22px;
    background: var(--brand-blue);
  }
  .brand-name {
    font-size: 30px;
    font-weight: 400;
    color: var(--brand-blue);
  }

  .body-text {
    position: absolute;
    left: 56px;
    width: 1072px;
    font-size: 24px;
    line-height: 37px;
    color: var(--teal);
  }
  .intro { top: 146px; }
  .closing { top: 625px; }

  .table-caption {
    position: absolute;
    left: 179px;
    width: 780px;
    top: 237px;
    text-align: center;
    font-family: "PT Sans", sans-serif;
    font-size: 20px;
    color: var(--brown-text);
  }

  .content-table {
    position: absolute;
    left: 179px;
    top: 271px;
    width: 781px;
    border-collapse: collapse;
    table-layout: fixed;
  }
  .content-table th,
  .content-table td {
    border: 2px solid var(--brown);
    text-align: center;
  }
  .content-table th {
    height: 64px;
    background: var(--table-head);
    font-family: "PT Sans", sans-serif;
    font-weight: 400;
    font-size: 18px;
    color: var(--brown-text);
  }
  .content-table td {
    font-size: 18px;
    color: var(--teal);
    background: rgba(255, 255, 255, 0.35);
  }
  .content-table tr.row-1 td { height: 49px; }
  .content-table tr.row-2 td,
  .content-table tr.row-3 td { height: 64px; }
  .content-table tr.row-4 td { height: 63px; }

  .page-number {
    position: absolute;
    left: 1126px;
    top: 812px;
    width: 46px;
    height: 46px;
    background: var(--page-box);
    color: var(--brown-text);
    font-size: 20px;
    font-weight: 700;
    display: flex;
    align-items: center;
    justify-content: center;
  }

  .footer {
    position: absolute;
    left: 0;
    bottom: 0;
    width: 1200px;
    height: 28px;
    background: var(--brown);
    color: var(--footer-text);
    font-size: 16px;
    font-weight: 700;
    text-align: center;
    line-height: 28px;
  }
</style>
</head>
<body>
<div class="slide">
  <div class="backdrop" role="img" aria-label="Soft grey background with a scattered square tile pattern"></div>

  <h1 class="slide-title">PROJECT TITLE</h1>
  <div class="brand">
    <span class="brand-mark"></span>
    <span class="brand-name">Brindle Consulting</span>
  </div>
  <div class="header-rule"></div>

  <p class="body-text intro">Lorem ipsum dolor sit amet lorem ipsum dolor sit amet lorem ipsum dolor sit amet lorem ipsum dolor sit amet :</p>

  <div class="table-caption">TABLE CONTENT HERE</div>
  <table class="content-table">
    <thead>
      <tr><th>HEADING TEXT</th><th>HEADING TEXT</th><th>HEADING TEXT</th><th>HEADING TEXT</th></tr>
    </thead>
    <tbody>
      <tr class="row-1"><td>Sub-content here</td><td>Sub-content here</td><td>Sub-content here</td><td>Sub-content here</td></tr>
      <tr class="row-2"><td>Sub-content here</td><td>Sub-content here</td><td>Sub-content here</td><td>Sub-content here</td></tr>
      <tr class="row-3"><td>Sub-content here</td><td>Sub-content here</td><td>Sub-content here</td><td>Sub-content here</td></tr>
      <tr class="row-4"><td>Sub-content here</td><td>Sub-content here</td><td>Sub-content here</td><td>Sub-content here</td></tr>
    </tbody>
  </table>

  <p class="body-text closing">Lorem ipsum dolor sit amet lorem ipsum dolor sit amet lorem ipsum dolor sit amet lorem ipsum dolor sit amet lorem ipsum dolor sit amet lorem ipsum dolor sit amet lorem ipsum dolor sit amet lorem ipsum dolor sit amet lorem ipsum dolor sit amet lorem ipsum dolorsit amet lorem ipsum dolor sit amet lorem ipsum dolor sit amet.</p>

  <div class="page-number">02</div>
  <footer class="footer">Copyright text here</footer>
</div>
</body>
</html>
```